Each Lady Ought to Learn Her R.I.M.shape

We need a book cover design for a book that will be used as a confidence coaching tool for women of all races, and walks of life . The title is a play on words because CUP is an acronym that stands for calling, uniqueness, and her purpose. The twist of the book is that this is from a male perspective.
The book will focus on Knowing the Bra types available and how bras represent the different kind of people you need in your life.
Updates

There are certain dynamics requested for this book cover i.e., tape measure, bra etc.  Please view pictures attached to file. i would like to see a book cover with breast covered maybe with hands. 

Target Market(s)

every female in the population of the world from every walk of life from 12-99

Requirements
Must have
• The book cover will also be used for the product line i.e. follow up work book and teaching tools. Measuring tapes, bras and breast are the main theme. Not too explicit that it wont be allowed on the shelves at Pellman and Crowe but I do want it to push the envelope TO THE POINT IT MAKES YOU WANT TO PICK IT UP!
Nice to have
• a woman measuring her breast or bust line .......also bra sizes like 36c 44dd 38b ect.
Should not have
• no naked women or faces of women or below the navel or above the neck pictures if breast revealed they must be covered by hands or bra or flowers ect.

```html
<!DOCTYPE html>
<html lang="en">
<head>
<meta charset="utf-8">
<title>Each Lady Ought to Learn Her R.I.M.shape — Book Cover</title>
<link rel="stylesheet" href="https://fonts.googleapis.com/css2?family=Jost:wght@400&display=swap">
<style>
  :root {
    --page-bg: #e9ebec;
    --cover-dark: #23292d;
    --sky-blue: #b8def0;
    --skin-light: #f3d2bd;
    --skin-mid: #e9b796;
    --tape-orange: #f26a0f;
    --tape-yellow: #fbbd2a;
    --title-blue: #c4e6f5;
    --accent-gold: #f5b321;
  }
  * { margin: 0; padding: 0; box-sizing: border-box; }
  html, body {
    width: 1200px; height: 1000px; overflow: hidden;
    background: var(--page-bg);
  }
  .canvas { position: relative; width: 1200px; height: 1000px; }
  .book-cover {
    position: absolute; left: 300px; top: 55px;
    width: 600px; height: 890px;
    background: var(--cover-dark);
    overflow: hidden;
    box-shadow: 0 6px 24px rgba(0,0,0,0.25);
    font-family: "Jost", "Futura", sans-serif;
    font-weight: 400;
  }
  .cover-art { position: absolute; inset: 0; }
  .cover-text {
    position: absolute; left: 0; right: 0; top: 568px;
    text-align: center; text-transform: uppercase; line-height: 1;
  }
  .cover-text h1 { font-weight: 400; }
  .author {
    color: var(--accent-gold); font-size: 19px; letter-spacing: 3px;
    text-align: left; padding-left: 60px; margin-bottom: 4px;
  }
  .title-lead {
    display: block;
    color: var(--title-blue); font-size: 60px; letter-spacing: 1px;
  }
  .title-mid {
    display: block;
    color: var(--title-blue); font-size: 29px; letter-spacing: 0.5px;
    margin-top: 6px;
  }
  .title-main {
    display: block;
    font-size: 90px; letter-spacing: 0; margin-top: 4px;
    white-space: nowrap;
  }
  .title-main .acronym { color: var(--accent-gold); }
  .title-main .word { color: var(--title-blue); }
  .subtitle {
    color: var(--accent-gold); font-size: 22px; letter-spacing: 3px;
    margin-top: 4px;
  }
</style>
</head>
<body>
<main class="canvas">
  <article class="book-cover">
    <svg class="cover-art" width="600" height="890" viewBox="0 0 600 890">
      <defs>
        <linearGradient id="photoTone" x1="0" y1="0" x2="1" y2="1">
          <stop offset="0" stop-color="#b8def0"/>
          <stop offset="0.35" stop-color="#f3d2bd"/>
          <stop offset="0.75" stop-color="#e9b796"/>
          <stop offset="1" stop-color="#b8def0"/>
        </linearGradient>
        <linearGradient id="tapeTone" x1="0" y1="0" x2="1" y2="0">
          <stop offset="0" stop-color="#f26a0f"/>
          <stop offset="0.45" stop-color="#fbbd2a"/>
          <stop offset="1" stop-color="#f26a0f"/>
        </linearGradient>
      </defs>

      <polygon class="cover-photo" points="0,0 600,0 600,470 0,315"
               fill="url(#photoTone)" role="img"
               aria-label="Photo of a woman's bare torso with her hands covering her chest, against a light blue background"/>

      <polygon class="tape-measure" points="0,315 600,470 600,560 0,410"
               fill="url(#tapeTone)" role="img"
               aria-label="Orange and yellow measuring tape wrapped diagonally across the torso"/>
    </svg>

    <header class="cover-text">
      <p class="author">Jane Doe</p>
      <h1>
        <span class="title-lead">Each Lady</span>
        <span class="title-mid">Ought to Learn Her</span>
        <span class="title-main"><span class="acronym">R.I.M</span><span class="word">Shape</span></span>
      </h1>
      <p class="subtitle">Resolve. Identity. Mission</p>
    </header>
  </article>
</main>
</body>
</html>
```